Health & Fitness Author & Public Speaker Needs Visually Stunning Web Design!

We've FINALLY got around to launching a website for Marisol Kettering - Australian Food Coach and Health & Fitness Expert. The website is to promote her new healthy eating program - "Bright Plate Living".
For a compehensive outline of exactly what we are after, please see the following attached files:
(1) Web Layout (wireframe, content/copy, links to photos to use, sample page we love)
(2) Style Guide (these are the colours, and overall feel we want)
Photos that we'd like used (of Marisol, and food/meals) can be found at these URL's:
Profile: https://www.filecrate.net/sh/q4r8vzkp2w7ttc3/H5M2xpLbeq
PixVault: https://www.filecrate.net/sh/b7mfwqjd3ue58an/9pq4Rtyhh2
HINT:
Before you do ANYTHING - check out this site as it is pretty much EXACTLY what we're after, but with our branding/colours/style: http://tovahlund.net/
As we will need to revamp our existing Chatterbook page & other printed material, there may be the potential for further work for the successful designer in the future.
Thanks & Good Luck!
Dorian Welch
Marketing & Business Development Manager
Bright Plate Living
Target Market(s)
Women, Ages 24 - 45, Interested in Healthly Eating & Fitness
Industry/Entity Type
Business
Look and feel
Each slider illustrates characteristics of the customer's brand and the style your logo design should communicate.

```html
<!DOCTYPE html>
<html lang="en">
<head>
<meta charset="utf-8">
<title>Bright Plate Living</title>
<link rel="stylesheet" href="https://fonts.googleapis.com/css2?family=Open+Sans:ital,wght@0,300;0,400;0,600;0,700;0,800;1,700&family=Dancing+Script:wght@600&display=swap">
<style>
:root{
  --pink:#ee1c5a;
  --rose:#c8385e;
  --lime:#8cc63f;
  --lime-bright:#b5dc3c;
  --teal:#4fcde0;
  --teal-light:#7fe0ee;
  --teal-dark:#2fb7cc;
  --ink:#444;
  --text:#6a6a6a;
  --dark:#333;
  --page:#fff;
  --side:#b4b4b4;
}
*{box-sizing:border-box;margin:0;padding:0}
html,body{width:930px;height:1200px;overflow:hidden}
body{position:relative;font-family:"Open Sans",Arial,sans-serif;color:var(--ink);
  background:linear-gradient(90deg,#9a9a9a 0,#d8d8d8 45px,#c4c4c4 85px,#d0d0d0 100%)}
.abs{position:absolute}
.side-lines{position:absolute;top:0;bottom:0;width:16px;
  background:repeating-linear-gradient(90deg,#fff 0 2px,#cfcfcf 2px 5px)}
.page{position:absolute;left:103px;top:0;width:727px;height:1200px;background:var(--page)}
.brand{left:153px;top:44px;font-size:21px;font-weight:600;color:var(--pink);letter-spacing:-.3px}
.nav a{position:absolute;top:39px;height:24px;line-height:24px;font-size:14px;color:var(--ink);text-decoration:none;font-weight:300}
.nav .active{background:var(--pink);color:#fff;padding:0 12px;font-weight:400}
.hero{left:148px;top:88px;width:634px;height:330px;
  background:linear-gradient(160deg,#cfe3a8 0%,#a5c97a 35%,#8fb35c 60%,#b5c98a 100%)}
.hero-copy{left:180px;top:129px;width:268px;height:268px;border-radius:50%;background:var(--lime);opacity:.95;color:#fff;text-align:center}
.hero-copy p{position:absolute;left:0;right:0;line-height:1}
.dot{position:absolute;top:405px;width:8px;height:8px;border-radius:50%;background:#fff}
.band{left:138px;top:418px;width:656px;height:77px;background:var(--teal);color:#fff}
.band h2{position:absolute;left:23px;top:12px;font-size:17px;font-weight:300;white-space:nowrap}
.band .sub{position:absolute;left:23px;top:36px;font-size:10.5px;font-weight:300}
.band .sub2{position:absolute;left:23px;top:52px;font-size:12px}
.field{position:absolute;background:#fff;border:0;font-size:9px;color:#888;padding:2px 6px;font-weight:300;font-family:inherit}
.btn-hook{left:663px;top:444px;width:107px;height:31px;border-radius:4px;background:var(--lime-bright);color:#fff;font-weight:800;font-size:13px;text-align:center;line-height:31px}
.photo{position:absolute}
.feature h3{position:absolute;left:355px;top:511px;width:220px;font-size:19px;font-weight:300;line-height:1.3;color:var(--ink)}
.body-copy{position:absolute;font-size:8.2px;line-height:1.52;color:var(--text);text-align:justify;font-weight:400}
.pager{position:absolute;top:643px;width:19px;height:23px;background:#666}
.post h4{position:absolute;font-size:15px;font-weight:300;line-height:1.2;color:var(--ink)}
.post .meta{position:absolute;font-size:8.4px;color:var(--text)}
.guide{left:582px;top:501px;width:197px;height:155px;background:linear-gradient(180deg,#f2f8d8,#e6f2c2)}
.challenge{left:582px;top:685px;width:197px;height:166px;background:var(--teal-light);color:#fff;text-align:center}
.join{left:582px;top:861px;width:197px;height:167px;background:var(--dark);color:#fff;border-bottom:4px solid var(--rose)}
.footer{left:103px;top:1156px;width:727px;height:44px;background:#3a3a3a;color:#fff}
.footer .links{position:absolute;left:0;right:0;top:15px;text-align:center;font-size:10.5px;font-weight:300;padding-right:94px}
.social{position:absolute;top:1175px;width:16px;height:16px;background:#fff;border-radius:2px}
</style>
</head>
<body>
<div class="side-lines" style="left:84px"></div>
<div class="side-lines" style="left:832px"></div>
<div class="page"></div>

<div class="abs brand">Bright Plate Living</div>
<nav class="nav">
  <a class="active" style="left:491px">Home</a>
  <a style="left:587px">About</a>
  <a style="left:663px">The Plan</a>
  <a style="left:750px">Shop</a>
</nav>

<div class="abs hero" role="img" aria-label="Photo of Marisol Kettering sitting on the grass in a sunny park"></div>
<div class="abs hero-copy">
  <p style="top:60px;font-size:36px;font-weight:300">GET SLIM</p>
  <p style="top:99px;font-size:46px;font-weight:800;letter-spacing:1px">BOOST</p>
  <p style="top:137px;font-size:43px;font-weight:800">ENERGY</p>
  <p style="top:180px;font-size:19px;font-weight:700">GUILT FREE WITH</p>
  <p style="top:207px;font-size:15px;font-weight:300">BRIGHT PLATE LIVING!</p>
  <p style="top:228px;font-size:15px;font-family:'Dancing Script',cursive">With Marisol Kettering</p>
</div>
<span class="dot" style="left:559px"></span><span class="dot" style="left:574px"></span><span class="dot" style="left:590px;background:transparent;border:1.5px solid #fff"></span><span class="dot" style="left:605px"></span>

<svg class="abs" style="left:138px;top:410px" width="656" height="8">
  <polygon points="0,8 10,0 10,8" fill="#2a9fb3"/>
  <polygon points="646,0 656,8 646,8" fill="#2a9fb3"/>
</svg>
<section class="abs band">
  <svg class="abs" style="left:23px;top:16px" width="17" height="12" viewBox="0 0 17 12"><rect x=".7" y=".7" width="15.6" height="10.6" fill="none" stroke="#fff" stroke-width="1.2"/><path d="M.7 .7 8.5 7 16.3 .7" fill="none" stroke="#fff" stroke-width="1.2"/></svg>
  <h2 style="left:45px">Join the Bright Plate Living Movement!</h2>
  <p class="sub">geat a weekly serving of Inspiration &amp; Advice that will change your life....</p>
  <p class="sub2">Bringing it on!</p>
</section>
<div class="field" style="left:513px;top:436px;width:131px;height:17px">Name</div>
<div class="field" style="left:513px;top:460px;width:131px;height:17px">email address</div>
<div class="abs btn-hook">HOOK ME UP!</div>

<section class="feature">
  <div class="photo" style="left:148px;top:516px;width:191px;height:150px;background:linear-gradient(135deg,#8a8478,#5e5a52)" role="img" aria-label="Photo of Marisol Kettering stretching by a stone wall"></div>
  <h3>Lorem Ipsum is simply dummy text</h3>
  <p class="body-copy" style="left:355px;top:562px;width:198px;text-align:left">Lorem Ipsum is simply dummy text of the printing and typesetting industry. Lorem Ipsum has been the industry's standard dummy text ever since the 1500s, when an unknown printer took a galley of type and scrambled it to make a type specimen book. It has survived not only five centuries</p>
  <svg class="pager" style="left:529px" viewBox="0 0 19 23"><path d="M11 7 7 11.5 11 16" fill="none" stroke="#ddd" stroke-width="1.2"/></svg>
  <svg class="pager" style="left:549px" viewBox="0 0 19 23"><path d="M8 7 12 11.5 8 16" fill="none" stroke="#ddd" stroke-width="1.2"/></svg>
</section>

<div class="photo" style="left:148px;top:677px;width:131px;height:118px;background:linear-gradient(135deg,#c9a06a,#e8e2d4 55%,#c8563a)" role="img" aria-label="Photo of a bowl of rice and vegetables with ginger and chillies"></div>
<div class="photo" style="left:292px;top:677px;width:131px;height:118px;background:linear-gradient(180deg,#c6d9a6,#8fae62)" role="img" aria-label="Photo of Marisol Kettering sitting on the lawn"></div>
<div class="photo" style="left:436px;top:677px;width:131px;height:118px;background:linear-gradient(135deg,#e7e2da,#d9c4a8 60%,#c8a98a)" role="img" aria-label="Photo of oats with raspberries and blueberries in a white bowl"></div>

<article class="post">
  <h4 style="left:148px;top:808px;width:131px">There are many variations</h4>
  <p class="meta" style="left:149px;top:847px">30/12/12 &nbsp; By : Marisol Kettering</p>
  <p class="body-copy" style="left:148px;top:865px;width:131px">Lorem Ipsum is simply dummy text of the printing and typesetting industry. Lorem Ipsum has been the industry's standard dummy text ever since the 1500s, when an unknown printer took a galley of type</p>
  <h4 style="left:292px;top:808px;width:140px">The standard chunk Lorem Ipsum</h4>
  <p class="meta" style="left:293px;top:847px">30/12/12 &nbsp; By : Marisol Kettering</p>
  <p class="body-copy" style="left:292px;top:865px;width:131px">Lorem Ipsum is simply dummy text of the printing and typesetting industry. Lorem Ipsum has been the industry's standard dummy text ever since the 1500s, when an unknown printer took a galley of type</p>
  <h4 style="left:436px;top:808px;width:131px">This book is one of treatise</h4>
  <p class="meta" style="left:437px;top:847px">30/12/12 &nbsp; By : Marisol Kettering</p>
  <p class="body-copy" style="left:436px;top:865px;width:131px">Lorem Ipsum is simply dummy text of the printing and typesetting industry. Lorem Ipsum has been the industry's standard dummy text ever since the 1500s, when an unknown printer took a galley of type</p>

  <h4 style="left:148px;top:973px;width:131px">There are many variations</h4>
  <p class="meta" style="left:149px;top:1012px">30/12/12 &nbsp; By : Marisol Kettering</p>
  <p class="body-copy" style="left:148px;top:1030px;width:131px">Lorem Ipsum is simply dummy text of the printing and typesetting industry. Lorem Ipsum has been the industry's standard dummy text ever since the 1500s, when an unknown printer took a galley of type</p>
  <h4 style="left:292px;top:973px;width:140px">The standard chunk Lorem Ipsum</h4>
  <p class="meta" style="left:293px;top:1012px">30/12/12 &nbsp; By : Marisol Kettering</p>
  <p class="body-copy" style="left:292px;top:1030px;width:131px">Lorem Ipsum is simply dummy text of the printing and typesetting industry. Lorem Ipsum has been the industry's standard dummy text ever since the 1500s, when an unknown printer took a galley of type</p>
  <h4 style="left:436px;top:973px;width:131px">This book is one of treatise</h4>
  <p class="meta" style="left:437px;top:1012px">30/12/12 &nbsp; By : Marisol Kettering</p>
  <p class="body-copy" style="left:436px;top:1030px;width:131px">Lorem Ipsum is simply dummy text of the printing and typesetting industry. Lorem Ipsum has been the industry's standard dummy text ever since the 1500s, when an unknown printer took a galley of type</p>
</article>

<aside class="abs guide">
  <p class="abs" style="left:0;right:0;top:18px;text-align:center;font-size:12px;color:#777">The ULTIMATE Bright Plate</p>
  <p class="abs" style="left:0;right:0;top:33px;text-align:center;font-size:22px;font-weight:700;color:var(--lime)">Eating Guide</p>
  <div class="abs" style="left:10px;top:80px;width:40px;height:72px;background:linear-gradient(180deg,#b6d85a,#5d9b2a)" role="img" aria-label="Photo of a green smoothie with kiwi"></div>
  <div class="abs" style="left:120px;top:88px;width:77px;height:67px;background:linear-gradient(135deg,#e7efd9,#9cc25a 50%,#e89a3a)" role="img" aria-label="Photo of a fresh salad plate"></div>
  <div class="abs" style="left:0;top:93px;width:132px;height:20px;background:var(--lime-bright);color:#fff;font-weight:800;font-size:11px;line-height:20px;padding-left:52px">GET IT NOW!</div>
</aside>

<aside class="abs challenge">
  <svg class="abs" style="left:60px;top:-12px" width="84" height="84"><circle cx="42" cy="42" r="39" fill="#ee6f8f" stroke="#fff" stroke-width="3"/></svg>
  <p class="abs" style="left:0;right:0;top:-4px;font-size:40px;font-weight:800;line-height:1.1">12</p>
  <p class="abs" style="left:0;right:0;top:44px;font-size:12px">WEEK</p>
  <p class="abs" style="left:0;right:0;top:68px;font-size:28px;font-weight:300">CHALLENGE</p>
  <p class="abs" style="left:0;right:0;top:103px;font-size:13px;line-height:1.1">Healthy, Happy<br>&amp; Hot In No <i style="font-weight:700">Time Flat!</i></p>
  <div class="abs" style="left:46px;top:140px;width:111px;height:19px;background:var(--teal-dark);font-size:12.5px;line-height:19px">JOIN US NOW!</div>
</aside>

<aside class="abs join">
  <p class="abs" style="left:18px;top:13px;font-size:17px;font-weight:300">JOIN THE MOVEMENT!</p>
  <p class="abs" style="left:18px;top:42px;width:168px;font-size:9.3px;line-height:1.35;font-weight:300">Join the Bright Plate Living Movement and get a free copy of The Kick Start Plan (valued $27.00)!</p>
  <div class="field" style="left:18px;top:83px;width:160px;height:16px">Name</div>
  <div class="field" style="left:18px;top:106px;width:160px;height:16px">email address</div>
  <div class="abs" style="left:46px;top:131px;width:111px;height:19px;background:var(--rose);border-radius:3px;text-align:center;font-size:12.5px;line-height:19px">SIGN ME UP!</div>
</aside>

<footer class="abs footer">
  <p class="links">Community &nbsp; | &nbsp; Free Resources &nbsp; | &nbsp; Press &nbsp; | &nbsp; Contact</p>
</footer>
<span class="social" style="left:734px" aria-label="Social link"></span>
<span class="social" style="left:760px" aria-label="Social link"></span>
<span class="social" style="left:786px" aria-label="Social link"></span>
</body>
</html>
```